meadowlarkVelmarun.com Blog/website

This is new site, we do not have any current content
Would like a website for meadowlark velmarun. The site will cover what to expect getting started, what to wear. How to pick out a velmarun Gym (called a box).
We will be posting articles on exercises and how to properly perform and occasional product review.
We would like a section on recipes and what to eat and not to eat
We are attempting to remove the barrier of entry to get new people transform their lives/body and try velmarun.
Will also like to post daily Work outs which are called WODs (workout of the day) and exercises.
The sections of the site I envision are
• the front landing page
• Contact Page
• Blog Page
• About Page
• Recipe Page
• Exercise Page
• FAQ and frequently used Terms

Target Market(s)

Fitness market, people interested or just starting velmarun

Industry/Entity Type

Fitness

Logo Text

meadowlark Velmarun - your velmarun start page - or something like that

Coding

Coded - Design and coding required

Number of Pages Required

5+ page

Font styles to use
Sans Serif

Requirements
Must have
• Frontpage, Contact Page, Blog Page, about page and FAQ and Terms Page
• This will be on a wordpress site
Nice to have
• would like to have more of a female slant and feel. photos of workouts

```html
<!DOCTYPE html>
<html lang="en">
<head>
<meta charset="utf-8">
<title>Velmarun Fitness Gym</title>
<link href="https://fonts.googleapis.com/css2?family=Source+Sans+Pro:wght@400;600;700&family=Syncopate:wght@700&display=swap" rel="stylesheet">
<style>
  :root{
    --red:#d71f27;
    --ink:#111111;
    --grey:#8a8a8a;
    --grey-light:#a5a5a5;
    --nav-bg:#f1f1f1;
    --search-bg:#dedede;
    --line:#e4e4e4;
    --white:#ffffff;
    --panel:rgba(190,190,190,0.72);
  }
  *{margin:0;padding:0;box-sizing:border-box}
  html,body{width:1089px;height:1200px;overflow:hidden;background:var(--white)}
  body{font-family:"Source Sans Pro",Arial,sans-serif;color:var(--grey);position:relative}
  a{text-decoration:none;color:inherit}

  .topbar{position:absolute;top:0;left:0;width:1089px;height:71px}
  .brand{position:absolute;left:74px;top:18px;font-size:34px;font-weight:400;letter-spacing:2px;color:var(--red);line-height:36px}
  .contact-strip{position:absolute;right:70px;top:25px;display:flex;align-items:center;font-size:15px;color:var(--grey);letter-spacing:.3px}
  .contact-strip .item{display:flex;align-items:center;gap:10px}
  .contact-strip .divider{width:1px;height:24px;background:var(--line);margin:0 18px}

  .mainnav{position:absolute;top:71px;left:0;width:1089px;height:47px;background:var(--nav-bg)}
  .mainnav ul{list-style:none;display:flex;position:absolute;left:72px;top:0;height:47px;align-items:center}
  .mainnav li{font-size:16px;color:var(--grey);margin-right:38px}
  .mainnav li.active{color:var(--red)}
  .search-btn{position:absolute;right:70px;top:0;width:47px;height:47px;background:var(--search-bg);display:flex;align-items:center;justify-content:center}

  .hero{position:absolute;top:118px;left:0;width:1089px;height:756px;overflow:hidden}
  .hero-photo{position:absolute;inset:0;background:
      radial-gradient(ellipse at 62% 35%,#8f8a86 0%,#5c5856 35%,#3a3837 70%,#2a2929 100%)}
  .hero-title{position:absolute;top:80px;left:0;width:100%;text-align:center;font-family:"Syncopate",Arial,sans-serif;font-weight:700;font-size:41px;color:var(--white);letter-spacing:1px}
  .hero-tagline{position:absolute;top:144px;left:0;width:100%;text-align:center;font-size:17px;letter-spacing:3.4px;color:var(--white)}

  .feature{position:absolute;top:215px;width:283px}
  .feature-photo{height:189px;position:relative}
  .feature-photo.people{background:linear-gradient(135deg,#2b3550,#1a1f2d 60%,#3a3a44)}
  .feature-photo.workout{background:linear-gradient(135deg,#d9d9d9,#a8a8a8 55%,#e6e6e6);border:1px solid var(--white)}
  .feature-photo.food{background:linear-gradient(135deg,#3d6b48,#7fa05c 45%,#c9c4b8 80%,#4b7f84)}
  .plus-btn{position:absolute;left:50%;top:50%;width:66px;height:66px;margin:-33px 0 0 -33px;border-radius:50%;background:var(--red);border:2px solid var(--white);display:flex;align-items:center;justify-content:center}
  .feature-body{margin-top:10px;height:189px;background:var(--panel);text-align:center;position:relative;padding-top:33px}
  .feature-body::before{content:"";position:absolute;top:-10px;left:50%;margin-left:-20px;border-left:20px solid transparent;border-right:20px solid transparent;border-bottom:10px solid var(--panel)}
  .feature-body h2{font-size:22px;font-weight:700;color:var(--ink);letter-spacing:.3px}
  .feature-body p{margin:18px auto 0;width:240px;font-size:13.2px;line-height:19px;color:var(--ink)}

  .footer-col{position:absolute;top:920px}
  .footer-col h3{font-size:17px;font-weight:400;color:var(--red);letter-spacing:.8px}
  .links{display:grid;grid-template-columns:123px 100px;row-gap:8px;margin-top:22px;font-size:15px;color:var(--grey)}
  .links .active{color:var(--red)}
  .touch p{margin-top:20px;width:300px;font-size:15px;line-height:19px;color:var(--grey);letter-spacing:.2px}
  .subscribe{margin-top:15px;margin-left:-2px;width:236px;height:34px;border:1px solid #cfcfcf;display:flex;align-items:center;justify-content:space-between;padding:0 14px 0 9px;font-size:13px;color:var(--grey);letter-spacing:.5px}
  .location dl{margin-top:22px;display:grid;grid-template-columns:66px 160px;row-gap:6px;font-size:12.5px;line-height:19px}
  .location dt{color:var(--ink)}
  .location dd{color:var(--grey-light)}

  .rule{position:absolute;top:1109px;left:0;width:1089px;height:1px;background:var(--line)}
  .copyright{position:absolute;top:1147px;left:72px;font-size:12.5px;color:var(--grey)}
  .copyright span{color:var(--red)}
  .social{position:absolute;top:1139px;right:69px;display:flex;gap:5px}
  .social span{width:33px;height:33px;border:1px solid #dcdcdc;display:block}
  .social span.active{border-color:var(--red)}
</style>
</head>
<body>
  <header class="topbar">
    <div class="brand">VELMARUN</div>
    <div class="contact-strip">
      <div class="item">
        <svg width="20" height="20" viewBox="0 0 20 20" fill="none" stroke="#d71f27" stroke-width="1.6"><path d="M4 2l3 3-2 3c1 3 3 5 6 6l2-2 3 3-2 3C8 18 2 12 2 4z"/></svg>
        +91 5550142736
      </div>
      <div class="divider"></div>
      <div class="item">
        <svg width="20" height="20" viewBox="0 0 20 20" fill="none" stroke="#d71f27" stroke-width="1.6"><path d="M18 2L2 9l6 2 2 7zM8 11l10-9"/></svg>
        hello@velmarun.net
      </div>
    </div>
  </header>

  <nav class="mainnav">
    <ul>
      <li class="active">Home</li><li>About Us</li><li>Exercise</li><li>Recipes</li><li>FAQ</li><li>Blog</li><li>Contact Us</li>
    </ul>
    <div class="search-btn">
      <svg width="15" height="15" viewBox="0 0 16 16" fill="none" stroke="#d71f27" stroke-width="2.2"><circle cx="6.5" cy="6.5" r="4.5"/><path d="M10 10l4 4"/></svg>
    </div>
  </nav>

  <section class="hero">
    <div class="hero-photo" role="img" aria-label="Blurred photo of an athlete training on a cable machine in a gym"></div>
    <h1 class="hero-title">VELMARUN FITNESS GYM</h1>
    <p class="hero-tagline">PUSH YOURSELF TO YUR LIMITS ACHIVE YOUR FITNESS GOALS</p>

    <article class="feature" style="left:89px">
      <div class="feature-photo people" role="img" aria-label="Photo of a female and a male athlete posing together"></div>
      <div class="feature-body">
        <h2>WHO WE ARE</h2>
        <p>Lorem ipsum dolor sit amet, consectetur adipiscing elit, sed do eiusmod tempor incididunt ut labore et dolore magna aliqua</p>
      </div>
    </article>

    <article class="feature" style="left:403px">
      <div class="feature-photo workout" role="img" aria-label="Photo of a woman doing a workout on a gym bench">
        <div class="plus-btn"><svg width="20" height="20" viewBox="0 0 20 20" stroke="#fff" stroke-width="4"><path d="M10 1v18M1 10h18"/></svg></div>
      </div>
      <div class="feature-body">
        <h2>OUR EXERCISES</h2>
        <p>Lorem ipsum dolor sit amet, consectetur adipiscing elit, sed do eiusmod tempor incididunt ut labore et dolore magna aliqua</p>
      </div>
    </article>

    <article class="feature" style="left:714px">
      <div class="feature-photo food" role="img" aria-label="Photo of a fresh salad with greens and radishes on a plate"></div>
      <div class="feature-body">
        <h2>SEE OUR RECIPES</h2>
        <p>Lorem ipsum dolor sit amet, consectetur adipiscing elit, sed do eiusmod tempor incididunt ut labore et dolore magna aliqua</p>
      </div>
    </article>
  </section>

  <footer>
    <div class="footer-col" style="left:72px">
      <h3>QUICK LINKS</h3>
      <div class="links">
        <span class="active">Home</span><span>FAQ</span>
        <span>About Us</span><span>Blog</span>
        <span>Exercise</span><span>Contact Us</span>
        <span>Recipes</span><span></span>
      </div>
    </div>
    <div class="footer-col touch" style="left:410px">
      <h3>KEEP IN TOUCH</h3>
      <p>Lorem ipsum dolor sit amet, consectetur adipiscing elit, sed do</p>
      <div class="subscribe">EMAIL ID
        <svg width="16" height="16" viewBox="0 0 20 20" fill="none" stroke="#8a8a8a" stroke-width="1.5"><path d="M18 2L2 9l6 2 2 7zM8 11l10-9"/></svg>
      </div>
    </div>
    <div class="footer-col location" style="left:798px">
      <h3>OUR LOCATION</h3>
      <dl>
        <dt>Address :</dt><dd>Lorem ipsum dolor sit amet, consectetur adipiscing elit</dd>
        <dt>Contact :</dt><dd>+91 5550142736</dd>
        <dt>Email ID :</dt><dd>hello@velmarun.net</dd>
      </dl>
    </div>
    <div class="rule"></div>
    <div class="copyright">© <span>VELMARUN</span> - 2016. All rights Reserved.</div>
    <div class="social"><span></span><span class="active"></span><span></span><span></span></div>
  </footer>
</body>
</html>
```